Redesign vq7.ch agency website for unique design with speed and conversion

We want to redesign our website vq7.ch. Our omnichannel marketing agency builds webshops and integrates them into existing systems like ERP/CRM and supports with online marketing campaigns like brixel ads and social media. The target of the redesign is to get a great look and feel for customers to see directly what we do, (please design something for our three focus areas eCommerce, Online marketing and Integration)
and to improve the pages speed drastically for SEO. Please see our attachment.
Target Market(s)
B2B
Industry/Entity Type
eCommerce Agency
Coding
Coded - Design and coding required
Number of Pages Required
5+ page
Look and feel

```html
<!DOCTYPE html>
<html lang="en">
<head>
<meta charset="utf-8">
<title>vq7 – Online Marketing Agentur Zürich</title>
<link href="https://fonts.googleapis.com/css2?family=Poppins:wght@400;500;600;700;800&display=swap" rel="stylesheet">
<style>
:root{
  --green:#4ade57;
  --green-soft:#d9f8dd;
  --teal:#0bbed8;
  --ink:#1b1d28;
  --text:#55585f;
  --muted:#8a8d94;
  --dark:#1d1f2b;
  --white:#fff;
  --line:#e6e8ec;
}
*{box-sizing:border-box;margin:0;padding:0}
html,body{width:1200px;height:4164px;overflow:hidden}
body{position:relative;background:var(--white);font-family:'Poppins',sans-serif;color:var(--ink)}
.abs{position:absolute}
a{color:inherit;text-decoration:none}

/* header */
.brand{position:absolute;font-weight:700;color:var(--green);letter-spacing:4px}
.site-logo{left:87px;top:22px;font-size:40px;line-height:46px}
.nav{position:absolute;left:350px;top:32px;display:flex;gap:34px;font-size:14px;font-weight:500}
.nav .active{color:var(--green)}
.lang{position:absolute;left:1010px;top:25px;width:101px;height:38px;border:1px solid var(--line);border-radius:19px;font-size:11px;font-weight:600;display:flex;align-items:center;justify-content:center;gap:8px}
.lang i{display:inline-block;width:14px;height:9px;background:#c7cbe0;border-radius:1px}

/* hero */
.hero-title{left:87px;top:206px;font-size:48px;line-height:53px;font-weight:700;width:480px}
.hero-sub{left:88px;top:384px;width:410px;font-size:13.5px;line-height:21px;color:var(--text)}
.btn{position:absolute;display:flex;align-items:center;justify-content:center;border-radius:22px;font-size:11px;font-weight:700;letter-spacing:.5px}
.btn-green{background:var(--green);color:var(--white)}
.btn-outline{border:2px solid var(--ink);color:var(--ink)}
.laptop{left:566px;top:96px;width:660px;height:482px}
.hero-blob{left:840px;top:560px;width:360px;height:230px}

/* service cards */
.card{position:absolute;background:var(--white);border-radius:14px;box-shadow:0 10px 30px rgba(20,30,40,.09);text-align:center}
.service{top:695px;width:240px;height:276px;padding:40px 24px 0}
.service svg{width:78px;height:68px}
.service h3{font-size:17px;font-weight:700;margin-top:22px}
.service p{font-size:11.5px;line-height:18.5px;color:var(--text);margin-top:14px}

/* about */
.photo{position:absolute;border-radius:50%}
.about-big{left:137px;top:1051px;width:430px;height:430px;background:linear-gradient(140deg,#e4e4e2,#b9bcc0 55%,#2c3548)}
.about-small{left:399px;top:1285px;width:240px;height:240px;background:linear-gradient(150deg,#d8d8d5,#8d939b 60%,#1f2a40);border:6px solid var(--white)}
.h2{position:absolute;font-size:36px;line-height:45px;font-weight:700}
.about-text{left:702px;width:355px;font-size:13px;line-height:20.5px;color:var(--text)}

/* values */
.values-band{left:0;top:1552px;width:1200px;height:431px}
.values-title{left:0;top:1712px;width:1200px;text-align:center;color:var(--white)}
.value{top:1795px;width:240px;height:329px;overflow:hidden}
.value .pic{height:188px}
.value h3{font-size:15px;font-weight:700;margin-top:30px}
.value p{font-size:11.5px;line-height:18.5px;color:var(--text);margin:14px 30px 0}

/* feedback */
.quote{left:173px;top:2340px;width:395px;font-size:15px;line-height:22px;color:var(--text)}
.client-name{left:173px;top:2444px;font-size:14px;font-weight:700}
.client-role{left:173px;top:2469px;font-size:12.5px;color:var(--text)}
.client-photo{left:605px;top:2215px;width:336px;height:336px;background:radial-gradient(circle at 50% 45%,#e9d6cc,#b9a49a 50%,#55504e)}

/* blog */
.blog-title{left:0;top:2612px;width:1200px;text-align:center}
.post{top:2681px;width:240px;height:346px;overflow:hidden;text-align:left}
.post .pic{height:189px}
.post .date{font-size:11px;color:var(--green);font-weight:600;margin:23px 24px 0}
.post h3{font-size:15px;font-weight:700;margin:8px 24px 0}
.post p{font-size:11.5px;line-height:18.5px;color:var(--text);margin:8px 24px 0}

/* partners */
.partners{position:absolute;left:87px;top:3130px;width:1022px;display:flex;justify-content:space-between;align-items:center}
.partner{display:flex;align-items:center;gap:8px;font-size:17px;font-weight:500;color:#5b5e66}
.partner i{width:14px;height:14px;border-radius:50%;background:#c9ccd2;display:inline-block}

/* contact */
.footer-bg{left:0;top:3400px;width:1200px;height:764px}
.form-box{left:181px;top:3292px;width:443px;height:476px;background:var(--green);border-radius:20px}
.field{position:absolute;background:var(--white);border-radius:21px;font-size:11.5px;color:#444;padding:0 18px;display:flex;align-items:center}
.field.area{border-radius:12px;align-items:flex-start;padding-top:14px}
.chat-title{left:702px;top:3326px}

/* footer */
.footer-logo{left:113px;top:3880px;font-size:66px;line-height:74px;letter-spacing:6px}
.social{position:absolute;top:3973px;width:32px;height:32px;border-radius:50%;background:#2e3140}
.f-col{position:absolute;top:3830px;color:var(--white)}
.f-col h4{font-size:19px;font-weight:700;margin-bottom:18px}
.f-col li{list-style:none;font-size:12px;line-height:31.5px;color:#d6d8de}
.f-col li::before{content:"›";margin-right:9px}
.info{display:flex;gap:10px;font-size:12px;line-height:17.5px;color:#d6d8de;margin-bottom:18px}
.info svg{flex:none;margin-top:3px}
.news p{font-size:12px;line-height:18px;color:#d6d8de;width:260px}
.news-input{margin-top:28px;width:260px;height:44px;background:var(--white);border-radius:22px;display:flex;align-items:center;padding:0 16px;gap:10px;font-size:11.5px;color:#555}
.news-input span{flex:1}
.divider{left:87px;top:4101px;width:1026px;height:1px;background:#3a3d4b}
.copyright{left:0;top:4122px;width:1200px;text-align:center;color:var(--white);font-size:12px}
.to-top{left:1133px;top:4082px;width:40px;height:40px;border-radius:50%;background:var(--green);display:flex;align-items:center;justify-content:center}
</style>
</head>
<body>

<header>
  <div class="brand site-logo">VQ7</div>
  <nav class="nav">
    <a class="active">Home</a><a>eCommerce</a><a>Online Marketing</a><a>Integration</a><a>Company ⌄</a><a>Contact Us</a>
  </nav>
  <div class="lang"><i></i>ENG <span>⌄</span></div>
</header>

<section class="hero">
  <h1 class="abs hero-title">Ihre online marketing agentur in zürich für KMUs</h1>
  <p class="abs hero-sub">Sie möchten Online die richtigen Menschen erreichen und mehr Umsatz generieren. Kontaktieren Sie uns!</p>
  <a class="btn btn-green" style="left:86px;top:451px;width:105px;height:42px">OFFERTE</a>
  <a class="btn btn-outline" style="left:200px;top:451px;width:105px;height:42px">TERMIN</a>
  <svg class="abs hero-blob" viewBox="0 0 360 230" aria-hidden="true">
    <defs><linearGradient id="hb" x1="0" y1="1" x2="1" y2="0"><stop offset="0" stop-color="#e9fbe9"/><stop offset="1" stop-color="#b8f3bd"/></linearGradient></defs>
    <path d="M20 230 C40 120 120 40 260 30 C310 26 340 20 360 10 L360 230Z" fill="url(#hb)"/>
    <path d="M60 230 C120 130 200 100 260 170 C300 220 340 200 360 180" fill="none" stroke="#a9eab0" stroke-width="1.5"/>
  </svg>
  <div class="abs laptop">
    <div class="abs" style="left:0;top:0;width:640px;height:470px;background:#222;border-radius:16px"></div>
    <div class="abs" role="img" aria-label="Photo of the two agency founders standing in front of a concrete wall" style="left:9px;top:9px;width:625px;height:440px;border-radius:10px;background:linear-gradient(120deg,#f2f2f1,#d7d8d6 45%,#b9bcbf 70%,#e6e6e5)"></div>
    <div class="abs" style="left:-56px;top:470px;width:716px;height:12px;background:linear-gradient(#b8bbc0,#6e7178);border-radius:0 0 10px 10px"></div>
  </div>
</section>

<section class="services">
  <div class="card service" style="left:218px">
    <svg viewBox="0 0 78 68" fill="none" stroke="#1b1d28" stroke-width="2.5"><rect x="4" y="4" width="70" height="46" rx="3"/><rect x="12" y="14" width="26" height="18" fill="#4ade57" stroke="none"/><path d="M46 16h20M46 24h20M46 32h14M12 40h54"/><circle cx="28" cy="60" r="3"/><circle cx="50" cy="60" r="3"/></svg>
    <h3>eCommerce</h3>
    <p>Do you want to sell your products or services online? But as an SME, don't you have a marketing departmen...</p>
  </div>
  <div class="card service" style="left:480px">
    <svg viewBox="0 0 78 68" fill="none" stroke="#1b1d28" stroke-width="2.5"><rect x="12" y="8" width="54" height="40" rx="3"/><path d="M4 56h70l-4 6H8z"/><rect x="20" y="16" width="38" height="24" fill="#4ade57" stroke="none"/><path d="M35 22l9 6-9 6z" fill="#fff" stroke="none"/></svg>
    <h3>Online marketing</h3>
    <p>In us you will find a dedicated team with passion, expertise and curiosity for all topics related to e-commerce...</p>
  </div>
  <div class="card service" style="left:740px">
    <svg viewBox="0 0 78 68" fill="none" stroke="#1b1d28" stroke-width="2.5"><circle cx="39" cy="34" r="20"/><circle cx="39" cy="34" r="10" fill="#4ade57" stroke="none"/><path d="M39 6v8M39 54v8M11 34h8M59 34h8M19 14l6 6M53 48l6 6M59 14l-6 6M25 48l-6 6"/></svg>
    <h3>Integration</h3>
    <p>Our goal is to give you added value with strategic online marketing – a technological competitive advantage...</p>
  </div>
</section>

<section class="about">
  <div class="photo about-big" role="img" aria-label="Portrait photo of a founder in a dark suit"></div>
  <div class="photo about-small" role="img" aria-label="Portrait photo of the second founder"></div>
  <h2 class="h2" style="left:702px;top:1070px">The fast way to<br>the online shop</h2>
  <p class="abs about-text" style="top:1178px">Our goal is to give you added value with strategic online marketing – a technological competitive advantage. Again that makes the difference. We build on automated processes for construction and operation</p>
  <p class="abs about-text" style="top:1296px">your online shop. In this way, we shorten project times, bring web shops online faster and simplify operations. This is how you get to your new web branch quickly and easily. You sell – we take care of it online</p>
  <a class="btn btn-green" style="left:702px;top:1426px;width:104px;height:42px">MORE</a>
</section>

<section class="values">
  <svg class="abs values-band" viewBox="0 0 1200 431" preserveAspectRatio="none" aria-hidden="true">
    <defs><linearGradient id="vb" x1="0" y1="0" x2="1" y2="0.3"><stop offset="0" stop-color="#4ee05a"/><stop offset="0.5" stop-color="#2fd18a"/><stop offset="1" stop-color="#0bbed8"/></linearGradient></defs>
    <path d="M0 40 C150 100 260 120 430 95 C620 65 720 0 920 8 C1060 14 1150 20 1200 0 L1200 20 C1100 40 1000 20 900 30 C700 50 600 120 420 130 C250 140 120 100 0 60Z" fill="#d6f7dc"/>
    <path d="M0 20 C150 90 260 140 430 112 C620 80 720 12 920 22 C1060 30 1150 28 1200 15 L1200 431 L0 431Z" fill="url(#vb)"/>
    <path d="M0 160 C60 130 110 150 110 220 C110 300 60 340 0 360Z" fill="#3fd24f" opacity=".5"/>
    <path d="M1200 150 C1140 160 1110 230 1140 300 C1160 340 1190 350 1200 350Z" fill="#0aaec6" opacity=".5"/>
  </svg>
  <h2 class="h2 values-title">Company values</h2>
  <div class="card value" style="left:218px">
    <div class="pic" role="img" aria-label="Photo of a consultant writing on a whiteboard" style="background:linear-gradient(120deg,#eef0f1,#cfd4d8 60%,#9aa3ab)"></div>
    <h3>Sustainability</h3><p>We help companies to sell products and services in their own online shop...</p>
  </div>
  <div class="card value" style="left:480px">
    <div class="pic" role="img" aria-label="Photo of a laptop with the agency sticker on a desk" style="background:linear-gradient(160deg,#2b3440,#1c7fa8 55%,#68c7d9)"></div>
    <h3>Quality</h3><p>We help companies to sell products and services in their own online shop...</p>
  </div>
  <div class="card value" style="left:740px">
    <div class="pic" role="img" aria-label="Photo of a bright office with people working at a table" style="background:linear-gradient(140deg,#f3f3f1,#c9ccc8 55%,#7d8b96)"></div>
    <h3>Customer orientation</h3><p>We help companies to sell products and services in their own online shop...</p>
  </div>
</section>

<section class="feedback">
  <h2 class="h2" style="left:173px;top:2275px">Customer feedback</h2>
  <p class="abs quote">It fully meets my expectations. The cooperation was professional and uncomplicated. Again any time. Already have several positive feedbacks for the</p>
  <p class="abs client-name">Marta Keller – owner of LUMA</p>
  <p class="abs client-role">Occupational therapy and speech therapy</p>
  <div class="photo client-photo" role="img" aria-label="Portrait photo of the client"></div>
  <svg class="abs" style="left:866px;top:2222px" width="155" height="104" viewBox="0 0 155 104" aria-hidden="true" fill="#4ade57">
    <circle cx="38" cy="66" r="36"/><path d="M10 50 C14 18 36 4 62 2 L62 14 C44 18 30 32 28 50Z"/>
    <circle cx="114" cy="66" r="36"/><path d="M86 50 C90 18 112 4 138 2 L138 14 C120 18 106 32 104 50Z"/>
  </svg>
</section>

<section class="blog">
  <h2 class="h2 blog-title">Latest blog</h2>
  <div class="card post" style="left:218px">
    <div class="pic" role="img" aria-label="Photo of two colleagues working at a laptop" style="background:linear-gradient(130deg,#d9dcde,#a6aeb6 55%,#6a6f78)"></div>
    <p class="date">15-01-2023</p><h3>Heading Goes Here</h3><p>We help companies to sell products and services in their own online shop...</p>
  </div>
  <div class="card post" style="left:480px">
    <div class="pic" role="img" aria-label="Photo of a meeting in a lounge with a yellow armchair" style="background:linear-gradient(130deg,#e6e2dc,#c7b27a 50%,#6f6a63)"></div>
    <p class="date">15-01-2023</p><h3>Heading Goes Here</h3><p>We help companies to sell products and services in their own online shop...</p>
  </div>
  <div class="card post" style="left:740px">
    <div class="pic" role="img" aria-label="Photo of a team discussion in a bright office" style="background:linear-gradient(130deg,#f1f1ef,#cdd0cf 55%,#5f6670)"></div>
    <p class="date">15-01-2023</p><h3>Heading Goes Here</h3><p>We help companies to sell products and services in their own online shop...</p>
  </div>
</section>

<section class="partners" aria-label="Partners">
  <span class="partner"><i></i>Brixel Ads</span>
  <span class="partner">Shoplane partners</span>
  <span class="partner"><i></i>Friendly Ads</span>
  <span class="partner"><i></i>Pick Partner</span>
  <span class="partner">Tallcart</span>
  <span class="partner">Wavecart</span>
</section>

<section class="contact">
  <svg class="abs footer-bg" viewBox="0 0 1200 764" preserveAspectRatio="none" aria-hidden="true">
    <path d="M0 80 C200 40 420 170 640 160 C860 150 1000 40 1200 20 L1200 764 L0 764Z" fill="#1d1f2b"/>
  </svg>
  <div class="abs form-box"></div>
  <div class="field" style="left:231px;top:3350px;width:167px;height:42px">First name</div>
  <div class="field" style="left:404px;top:3350px;width:167px;height:42px">Last name</div>
  <div class="field" style="left:231px;top:3404px;width:167px;height:42px">Phone</div>
  <div class="field" style="left:404px;top:3404px;width:167px;height:42px">Email</div>
  <div class="field" style="left:231px;top:3457px;width:340px;height:41px">Reference</div>
  <div class="field area" style="left:231px;top:3509px;width:340px;height:154px">Type your text</div>
  <a class="btn" style="left:333px;top:3684px;width:128px;height:38px;background:var(--dark);color:#fff">SENDEN</a>
  <h2 class="h2 chat-title">Let's chat<br>tell me about your<br>project</h2>
</section>

<footer>
  <div class="brand footer-logo">VQ7</div>
  <span class="social" style="left:159px" aria-label="Social network 1"></span>
  <span class="social" style="left:206px" aria-label="Social network 2"></span>
  <span class="social" style="left:251px" aria-label="Social network 3"></span>

  <div class="f-col" style="left:399px">
    <h4>Quick links</h4>
    <ul><li>Join Our Team</li><li>Privacy</li><li>Terms of Service</li><li>FAQs</li><li>Affiliates and Partners</li><li>Accessibility</li></ul>
  </div>
  <div class="f-col" style="left:601px">
    <h4>Contact info</h4>
    <div class="info"><svg width="12" height="10" viewBox="0 0 12 10"><rect width="12" height="10" rx="1" fill="#4ade57"/><path d="M0 1l6 4 6-4" stroke="#1d1f2b" fill="none"/></svg><span>Emai:<br>info@vq7.ch</span></div>
    <div class="info"><svg width="12" height="12" viewBox="0 0 12 12"><path d="M2 1l3 0 1 3-2 1.5c.8 1.6 1.9 2.7 3.5 3.5L9 7l3 1v3c-6 1-11-4-10-10z" fill="#4ade57"/></svg><span>Phone:<br>+41 44 000 12 34</span></div>
    <div class="info"><svg width="12" height="14" viewBox="0 0 12 14"><path d="M6 0a5 5 0 015 5c0 4-5 9-5 9S1 9 1 5a5 5 0 015-5z" fill="#4ade57"/><circle cx="6" cy="5" r="2" fill="#1d1f2b"/></svg><span>Location:<br>Lindenweg 12, 8000<br>Zurich, Switzerland</span></div>
  </div>
  <div class="f-col news" style="left:831px">
    <h4>Newsletter</h4>
    <p>Subscribe to our email address to get the latest news.</p>
    <div class="news-input"><svg width="14" height="11" viewBox="0 0 14 11"><rect x=".5" y=".5" width="13" height="10" rx="1" fill="none" stroke="#888"/><path d="M1 1l6 4 6-4" stroke="#888" fill="none"/></svg><span>Enter Your Email...</span><svg width="14" height="14" viewBox="0 0 14 14"><path d="M0 6L14 0 9 14 7 8z" fill="#4ade57"/></svg></div>
  </div>
  <div class="abs divider"></div>
  <p class="abs copyright">2023 vq7 Marketing GmbH.</p>
  <a class="abs to-top" aria-label="Back to top"><svg width="14" height="14" viewBox="0 0 14 14"><path d="M7 13V2M2 7l5-5 5 5" stroke="#fff" stroke-width="1.6" fill="none"/></svg></a>
</footer>

</body>
</html>
```